QWR Consulting Web Design… We need a Facelift!

We currently have a website but it is very outdated. We like our content, but could use some help on giving it a refreshed facelift.

www.QWR-Consulting.example is our site

We only consult with large companies in the US that have sales over $250,000 a year, so looking to be high end yet approachable in our look.

Target Market(s)

Large corporations

Industry/Entity Type

Consulting

Coding

Coded - Design and coding required

Number of Pages Required

5+ page

Font styles to use
Serif
Sans Serif

Requirements
Must have
• We love our logo, keep that the same.
• The site colors can deviate from the logo, as long as it is complimentary
Nice to have
• We like our videos and graphics. If you can make them better, then great! But you can also feel free to reuse them.
• There is a video on the opening screen and one on the video page.
• We would like the video on the video page to be incorporated on the first page.
• If you think we need other/more page, we are all ears!
Should not have
• Want to set us apart from our competition in look, feel, professionalism and step away from the old fashioned conservatives of their websites. We want to be professional, yet bolder and fresher.
• Our Competition is LedgerBrook.example and TheHallowayPartners.example, but not looking to copy of emulate them, but gives an idea of the world QWR is in.

```html
<!DOCTYPE html>
<html lang="en">
<head>
<meta charset="utf-8">
<title>QWR Consulting</title>
<link href="https://fonts.googleapis.com/css2?family=Open+Sans:ital,wght@0,400;0,600;0,700;0,800;1,400&display=swap" rel="stylesheet">
<style>
:root{
  --blue:#4a7bc0;
  --blue-dark:#3a67a8;
  --red:#b7312c;
  --red-dark:#9c2622;
  --ink:#333;
  --muted:#666;
  --light:#f3f3f3;
  --footer:#2b2b2b;
  --white:#fff;
}
*{margin:0;padding:0;box-sizing:border-box}
html,body{width:1200px;height:2826px;overflow:hidden}
body{font-family:"Open Sans",Arial,sans-serif;color:var(--ink);background:var(--white);position:relative}
.abs{position:absolute}
/* header */
.header{left:0;top:0;width:1200px;height:160px;background:var(--white)}
.brand{left:100px;top:48px;display:flex;align-items:center;gap:14px}
.brand-dot{width:46px;height:46px;border-radius:50%;background:var(--red)}
.brand-name{font-size:26px;font-weight:700;color:var(--ink)}
.search{left:542px;top:65px;width:34px;height:34px;border-radius:50%;background:#eee}
.social-label{left:597px;top:75px;font-size:11px;color:var(--muted)}
.social-dot{top:69px;width:28px;height:28px;border-radius:50%}
.btn{display:flex;align-items:center;justify-content:center;background:var(--red);color:var(--white);font-size:13px;border-radius:3px}
.consult{left:933px;top:60px;width:169px;height:45px}
/* nav */
.nav{left:0;top:160px;width:1200px;height:58px;background:var(--blue)}
.nav a{position:absolute;top:0;height:58px;line-height:58px;color:var(--white);font-size:12px;text-decoration:none;transform:translateX(-50%)}
.nav a.active{background:var(--red);width:132px;text-align:center}
/* hero */
.hero{left:0;top:218px;width:1200px;height:534px;background:linear-gradient(100deg,#2a3340 0%,#3d4a5a 40%,#202833 100%)}
.hero-title{left:100px;top:543px;width:460px;height:112px;background:rgba(20,20,20,.72);padding:16px 24px}
.hero-title h1{font-size:32px;font-weight:800;color:var(--white);line-height:1.2}
.hero-title p{font-size:32px;font-weight:400;color:var(--white);line-height:1.2}
.arrow-dot{top:672px;width:16px;height:16px;border-radius:50%;background:#aaa}
.contact{left:785px;top:282px;width:316px;height:408px;background:rgba(15,15,15,.85)}
.contact h2{background:var(--blue);color:var(--white);font-size:16px;font-weight:600;height:46px;line-height:46px;text-align:center}
.field{position:absolute;left:26px;width:264px;height:37px;border:1px solid #ccc;border-radius:3px;color:var(--white);font-size:12px;padding:9px 14px}
.contact .btn{position:absolute;left:26px;top:330px;width:264px;height:40px;font-weight:600}
/* welcome */
.welcome{left:0;top:752px;width:1200px;height:558px;background:var(--light)}
.welcome h2{position:absolute;top:40px;width:1200px;text-align:center;font-size:25px;font-weight:400;color:var(--ink)}
.welcome .intro{position:absolute;left:130px;top:85px;width:940px;text-align:center;font-size:12px;line-height:22px;color:var(--muted)}
.card{top:190px;width:230px;text-align:center}
.card .pic{width:230px;height:154px;border:4px solid var(--white)}
.card h3{margin-top:20px;font-size:14px;font-weight:400;color:var(--blue)}
.card p{margin:14px auto 0;width:200px;font-size:11px;line-height:20px;color:var(--muted)}
.card .btn{margin:16px auto 0;width:102px;height:34px;font-size:11px}
/* video */
.video-head{left:100px;top:1350px}
.video-head h2{font-size:27px;font-weight:400;color:var(--red)}
.video-head p{font-size:12px;color:var(--muted);margin-top:8px}
.player{left:100px;top:1446px;width:395px;height:264px;background:#222;border:3px solid #ddd}
.player .screen{position:absolute;left:0;top:18px;width:389px;height:208px;background:linear-gradient(135deg,#f4f6f8,#c9d3de)}
.player .bar{position:absolute;left:0;bottom:0;width:389px;height:32px;background:#1c1c1c}
.play{left:155px;top:90px;width:80px;height:80px;border-radius:50%;background:rgba(0,0,0,.8);border:3px solid #fff}
.video-text{left:538px;top:1440px;width:560px;font-size:11px;line-height:21px;color:#888}
.video-text p+p{margin-top:10px}
.more{left:538px;top:1668px;width:159px;height:43px;font-size:11px}
/* testimonials */
.testi{left:0;top:1765px;width:1200px;height:310px;background:linear-gradient(180deg,#4e7ec4,#3f6fb4)}
.testi h2{position:absolute;top:52px;width:1200px;text-align:center;font-size:25px;font-weight:400;color:var(--white)}
.portrait{left:191px;top:1868px;width:150px;height:150px;border-radius:50%;background:linear-gradient(160deg,#d9c3b0,#8a6d58);border:6px solid var(--white)}
.quote{left:424px;top:1900px;width:530px;font-size:11px;font-style:italic;line-height:24px;color:var(--white)}
.quote-mark{font-size:44px;line-height:44px;color:#dbe6f5;font-family:Georgia,serif;font-style:normal}
.quote-mark.open{left:394px;top:1872px}
.quote-mark.close{left:962px;top:1944px}
.author{left:424px;top:1992px;font-size:10px;color:var(--white)}
/* why */
.why h2{position:absolute;top:2115px;width:1200px;text-align:center;font-size:25px;font-weight:400}
.why .sub{position:absolute;top:2162px;width:1200px;text-align:center;font-size:12px;color:var(--muted)}
.devices{left:104px;top:2204px;width:500px;height:452px;background:linear-gradient(160deg,#e9ecef,#c0c8d0);border-radius:8px}
.feature{left:672px;width:400px}
.feature svg{position:absolute;left:0;top:0}
.feature h3{position:absolute;left:127px;top:0;font-size:14px;font-weight:400;color:var(--blue)}
.feature p{position:absolute;left:127px;top:28px;width:260px;font-size:11px;line-height:22px;color:var(--muted)}
.scroll{left:1094px;top:2170px;width:4px;height:450px;background:#e4e4e4}
.scroll i{position:absolute;left:0;top:142px;width:4px;height:40px;background:#555}
/* footer */
.footer{left:0;top:2700px;width:1200px;height:126px;background:var(--footer)}
.f-dot{top:2716px;width:32px;height:32px;border-radius:50%;border:1px solid #777}
.f-links{top:2767px;width:1200px;text-align:center;font-size:10px;color:#bbb;word-spacing:2px}
.f-links span{margin:0 14px;color:#777}
.copy{top:2793px;width:1200px;text-align:center;font-size:9px;color:#999}
</style>
</head>
<body>

<header class="header abs">
  <div class="brand abs"><span class="brand-dot"></span><span class="brand-name">QWR-Consulting.example</span></div>
  <div class="search abs"></div>
  <div class="social-label abs">Connect with our social network</div>
  <span class="social-dot abs" style="left:779px;background:#3b5998"></span>
  <span class="social-dot abs" style="left:813px;background:#3aa0dd"></span>
  <span class="social-dot abs" style="left:847px;background:#e6a52b"></span>
  <span class="social-dot abs" style="left:881px;background:#1f76b4"></span>
  <div class="btn consult abs">Make A Consultation</div>
</header>

<nav class="nav abs">
  <a class="active" style="left:166px">HOME</a>
  <a style="left:333px">WHY QWR?</a>
  <a style="left:526px">OUR PROCESS</a>
  <a style="left:723px">CONTACT US</a>
  <a style="left:910px">ABOUT US</a>
  <a style="left:1080px">CLIENT</a>
</nav>

<section class="hero abs" role="img" aria-label="Businessman touching a rising green arrow over a financial chart"></section>
<div class="hero-title abs"><h1>COMPARATIVE ANALYSIS</h1><p>MODELING..!</p></div>
<span class="arrow-dot abs" style="left:99px"></span>
<span class="arrow-dot abs" style="left:120px"></span>
<form class="contact abs">
  <h2>CONTACT INFORMATION</h2>
  <div class="field" style="top:66px">First name</div>
  <div class="field" style="top:118px">Last name</div>
  <div class="field" style="top:174px">Email address</div>
  <div class="field" style="top:225px;height:90px">Message...</div>
  <div class="btn">CONTACT US</div>
</form>

<section class="welcome abs">
  <h2>Welcome to QWR-Consulting</h2>
  <p class="intro">QWR Consulting works closely with your team assisting in auditing your bank fees and earnings credit rates. As former bankers, we bring our primary and regional bank experience to the table to supplement your team in providing insider knowledge for various bank pricing and net cost thresholds, so you can negotiate better pricing, rates, and terms. Maximize return when you know your true banking costs.</p>
  <div class="card abs" style="left:104px">
    <div class="pic" role="img" aria-label="Hands reviewing market charts" style="background:linear-gradient(135deg,#e6edf5,#9fb6d2)"></div>
    <h3>Know The Market</h3>
    <p>Focusing on your business -- not on banking. Even in today's information age, it is exceedingly difficult to keep...</p>
    <div class="btn">Read More</div>
  </div>
  <div class="card abs" style="left:360px">
    <div class="pic" role="img" aria-label="Business handshake at a meeting table" style="background:linear-gradient(135deg,#d8d8d8,#555)"></div>
    <h3>Understand Profitability</h3>
    <p>Pricing is determined by profitability more than any other factor. QWR Consulting provides a Relationship...</p>
    <div class="btn">Read More</div>
  </div>
  <div class="card abs" style="left:616px">
    <div class="pic" role="img" aria-label="Treasury team meeting in an office" style="background:linear-gradient(135deg,#eef0f2,#5a6470)"></div>
    <h3>Augment Your Team</h3>
    <p>Add to what your treasury team is already doing. Your team may already have completed their own...</p>
    <div class="btn">Read More</div>
  </div>
  <div class="card abs" style="left:872px">
    <div class="pic" role="img" aria-label="Digital financial data graphic in blue" style="background:linear-gradient(135deg,#1d3f6e,#5a93c8)"></div>
    <h3>What Banks Want</h3>
    <p>Understand the many cards you have in your hand to play. Although bankers have an incentive to maximize...</p>
    <div class="btn">Read More</div>
  </div>
</section>

<div class="video-head abs">
  <h2>Our Video</h2>
  <p>Sed ut perspiciatis unde omnis iste natus error sit voluptatem accusantium doloremque laudantium, totam</p>
</div>
<div class="player abs">
  <div class="screen" role="img" aria-label="Video still of a presenter beside a treasury and cash management diagram"></div>
  <div class="play abs"><svg width="74" height="74" viewBox="0 0 74 74"><path d="M30 23 L52 37 L30 51 Z" fill="#fff"/></svg></div>
  <div class="bar"><svg width="389" height="32"><path d="M12 10 L22 16 L12 22 Z" fill="#ccc"/><rect x="80" y="14" width="220" height="3" fill="#555"/></svg></div>
</div>
<div class="video-text abs">
  <p>Sed ut perspiciatis unde omnis iste natus error sit voluptatem accusantium doloremque laudantium, totam rem aperiam, eaque ipsa quae ab illo inventore veritatis et quasi architecto beatae vitae dicta sunt explicabo. Nemo enim ipsam voluptatem quia voluptas sit aspernatur aut odit aut fugit, sed quia consequuntur magni Neque porro quisquam est, qui dolorem ipsum quia dolores eos qui ratione voluptatem sequi nesciunt...</p>
  <p>architecto beatae vitae dicta sunt explicabo. Nemo enim ipsam voluptatem quia voluptas sit aspernatur aut odit aut fugit, sed quia consequuntur magni dolores eos qui ratione voluptatem sequi nesciunt. Neque porro quisquam est, qui dolorem ipsum quia dolor sit labore et dolore magnam aliquam quaerat voluptatem. Ut enim ad minima veniam, quis nostrum exercitationem ullam corporis suscipit laboriosam, amet, consectetur, adipisci velit, sed quia non numquam eius modi tempora incidunt ...</p>
</div>
<div class="btn more abs">CLICK VIEW MORE</div>

<section class="testi abs"><h2>Client Testimonials</h2></section>
<div class="portrait abs" role="img" aria-label="Portrait photo of the client"></div>
<span class="quote-mark open abs">&ldquo;</span>
<div class="quote abs">"In the 20 years I've been in treasury management, I really felt that I'd mastered our bank pricing. But when I started understanding bank's profitability so that I could laser focus on line items or rates for discussion, it became a game changer."</div>
<span class="quote-mark close abs">&rdquo;</span>
<div class="author abs"><b>ALEX MARLOW</b> - Treasurer of a National Retail Department Store</div>

<section class="why">
  <h2>Why QWR?</h2>
  <p class="sub">Sed ut perspiciatis unde omnis iste natus error sit voluptatem accusantium doloremque laudantium, totam rem aperiam, e</p>
  <div class="devices abs" role="img" aria-label="Desktop monitor and tablet showing business meeting and chart imagery"></div>
  <div class="feature abs" style="top:2254px">
    <svg width="100" height="100"><circle cx="50" cy="50" r="44" fill="none" stroke="#8fb3e0" stroke-width="8"/><path d="M6 50 A44 44 0 0 0 94 50" fill="none" stroke="var(--red)" stroke-width="8"/><circle cx="50" cy="50" r="32" fill="#fff"/><g fill="var(--red)"><rect x="38" y="52" width="5" height="10"/><rect x="46" y="44" width="5" height="18"/><rect x="54" y="48" width="5" height="14"/><rect x="35" y="63" width="28" height="2"/></g></svg>
    <h3>Profitability</h3>
    <p>Clients enjoy gains they never thought possible by looking beyond market pricing and harnessing YieldMap™...</p>
  </div>
  <div class="feature abs" style="top:2400px">
    <svg width="100" height="100"><circle cx="50" cy="50" r="44" fill="none" stroke="#8fb3e0" stroke-width="8"/><path d="M6 50 A44 44 0 0 0 94 50" fill="none" stroke="var(--red)" stroke-width="8"/><circle cx="50" cy="50" r="32" fill="#fff"/><g fill="var(--red)"><path d="M34 44 L50 35 L66 44 Z"/><rect x="38" y="46" width="4" height="14"/><rect x="48" y="46" width="4" height="14"/><rect x="58" y="46" width="4" height="14"/><rect x="34" y="61" width="32" height="3"/></g></svg>
    <h3>Insiders</h3>
    <p>Our team has managed treasury personnel as well as client relationships from within banks.</p>
  </div>
  <div class="feature abs" style="top:2527px">
    <svg width="100" height="100"><circle cx="50" cy="50" r="44" fill="none" stroke="#8fb3e0" stroke-width="8"/><path d="M6 50 A44 44 0 0 0 94 50" fill="none" stroke="var(--red)" stroke-width="8"/><circle cx="50" cy="50" r="32" fill="#fff"/><g fill="none" stroke="var(--red)" stroke-width="3"><circle cx="50" cy="50" r="12"/><circle cx="50" cy="50" r="4" fill="var(--red)"/><path d="M50 32 V40 M50 60 V68 M32 50 H40 M60 50 H68"/></g></svg>
    <h3>Involved</h3>
    <p>Clients enjoy gains never possible before, with millions of dollars in actualized annual savings in their accounts...</p>
  </div>
  <div class="scroll abs"><i></i></div>
</section>

<footer class="footer abs"></footer>
<span class="f-dot abs" style="left:491px"></span>
<span class="f-dot abs" style="left:538px"></span>
<span class="f-dot abs" style="left:585px"></span>
<span class="f-dot abs" style="left:632px"></span>
<span class="f-dot abs" style="left:679px"></span>
<div class="f-links abs">HOME<span>/</span>WHY QWR?<span>/</span>OUR PROCESS<span>/</span>CONTACT US<span>/</span>ABOUT US<span>/</span>CLIENT</div>
<div class="copy abs">COPYRIGHTS © QWR-CONSULTING .2016 | ALLRIGHTS RESERVED</div>

</body>
</html>
```